The Quiet Ascent Book Cover

Book Title:
The Quiet Ascent: Lessons of Insight From A Circle of Mentors to Guide You Toward a Fuller Journey

This book will offer the wisdom and philosophies of a variety of different coaches to allow future clients to get a taste of you and your style and prepare them to work with you!

A coach does not fix you. Or heal you. They coach you - offer thoughts to ponder, guidance, techniques to try. All to help you plays and succeed at the game of life.

Each coach has their own personality, training, experience, method and philosophy they bring to the table. The underlying purpose is to guide you through The Quiet Ascent, to become the person you desire and aspire to be. Different coaches for different folks, yet they all have their own unique wisdom and special sauce to share.

This book is a collection of just that. A tasting of the wisdom and philosophies of a variety of different coaches for you to experience.

Types of Coaches: Clarity, Dreams, Goals, Motivation, Mindset,  Subconscious, Beliefs, Behavior, Accountability, Life, Wellness, Love & Dating, Relationships, Sex, Business, Career,  Executive,  Personal Development,  Writing, Wellness, Fitness, Parenting,  Style, Spirituality, Public Speaking, Financial,  Time management, Weight Loss, Running, Self esteem,  Tarot, Astrology, Enneagram, Soul path/ Dharma, Skills, Performance,  Speaking / Communication, Leadership, Shadow Work, Acting, Sports, ANY & ALL

Target Market(s)

Males or females looking for guidance and words of wisdom from an expert coach - maybe to find one that resonates with them to work with further. Ages 16 and up. Any Gender. International. Looking to improve their life!

Industry/Entity Type

Self Development, Wellness, Coaching, Personal Growth, Fitness, Spirituality, Business, Relationships

Font styles to use
Serif
Script

Colors
0054AA
0677BA
7BADD7
CADEEF
E8F1F8
FFF300
FFF600
FEFA6F
FFFEC7
FFFEE8

Requirements
Must have
• I am looking for a visually appealing, unique cover that encompasses the breadth and depth of the transformation that people can go through and inspires them to want to grow and change even more. I love when elegant and classic simplicity is combined with some kind of twist that catches the eye and provokes thought. I love complimentary fonts, colors, design elements. You can visit my Veltrano Author Page - Dr. Marisol Penbury Aldane to see my titles to see what I have liked! But I am also excited to see where you can make my vision even better!!
Nice to have
• Front Cover - Image, Title and Subtitle, The Lark Publishing House, Spine - Title and Publishing House Logo, Back - Book Blurb, Authors Names, Info about Publishing House, ISBN Barcode
Should not have
• Anything too feminine or too masculine as I want to encourage coaches of all genders to participate.

```html
<!DOCTYPE html>
<html lang="en">
<head>
<meta charset="UTF-8">
<title>The Quiet Ascent — Book Cover</title>
<link rel="stylesheet" href="https://fonts.googleapis.com/css2?family=Allura&family=Raleway:wght@200&family=PT+Sans+Narrow&family=Libre+Baskerville:wght@700&display=swap">
<style>
  :root {
    --stage: #ecebe8;
    --deep-blue: #1f2fb8;
    --royal-blue: #2f56d6;
    --sky-blue: #6f9fe6;
    --mist-blue: #a9c6f0;
    --spine-shadow: rgba(10, 20, 90, 0.45);
    --title-white: #ffffff;
    --title-gold: #f4d25a;
    --text-light: #eef3ff;
    --wing-pink: #e94fc8;
    --wing-glow: #f7c86a;
  }
  * { box-sizing: border-box; margin: 0; padding: 0; }
  html, body {
    width: 1200px;
    height: 800px;
    overflow: hidden;
    background: var(--stage);
  }
  .book-cover {
    position: absolute;
    left: 342px;
    top: 20px;
    width: 516px;
    height: 760px;
    overflow: hidden;
  }
  .cover-artwork {
    position: absolute;
    inset: 0;
    background:
      radial-gradient(ellipse 55% 35% at 42% 30%, var(--mist-blue) 0%, rgba(169,198,240,0) 70%),
      radial-gradient(ellipse 60% 40% at 60% 60%, var(--sky-blue) 0%, rgba(111,159,230,0) 75%),
      linear-gradient(160deg, var(--deep-blue) 0%, var(--royal-blue) 45%, var(--royal-blue) 70%, var(--deep-blue) 100%);
  }
  .spine-edge {
    position: absolute;
    left: 0; top: 0; bottom: 0;
    width: 14px;
    background: linear-gradient(90deg, var(--spine-shadow), rgba(10,20,90,0));
  }
  .title-block {
    position: absolute;
    left: 0; top: 0;
    width: 100%;
    height: 240px;
    font-weight: 400;
  }
  .title-the {
    position: absolute;
    left: 232px;
    top: 22px;
    font-family: "Allura", cursive;
    font-weight: 400;
    font-size: 56px;
    color: var(--title-gold);
    line-height: 1;
  }
  .title-quiet {
    position: absolute;
    left: 60px;
    top: 66px;
    font-family: "Allura", cursive;
    font-weight: 400;
    font-size: 140px;
    color: var(--title-white);
    line-height: 1;
  }
  .title-ascent {
    position: absolute;
    right: 44px;
    top: 172px;
    font-family: "Raleway", sans-serif;
    font-weight: 200;
    font-size: 62px;
    color: var(--title-gold);
    line-height: 1;
  }
  .butterfly-illustration {
    position: absolute;
    left: 25px;
    top: 222px;
    width: 466px;
    height: 280px;
  }
  .subtitle {
    position: absolute;
    left: 20px;
    right: 20px;
    top: 532px;
    font-family: "PT Sans Narrow", sans-serif;
    font-size: 23px;
    line-height: 33px;
    text-transform: uppercase;
    text-align: center;
    color: var(--text-light);
    letter-spacing: -0.3px;
  }
  .author {
    position: absolute;
    left: 0; right: 0;
    top: 640px;
    font-family: "PT Sans Narrow", sans-serif;
    font-size: 35px;
    text-transform: uppercase;
    text-align: center;
    color: var(--text-light);
    letter-spacing: -0.5px;
  }
  .publisher {
    position: absolute;
    left: 0; right: 0;
    top: 700px;
    display: flex;
    justify-content: center;
    align-items: center;
    gap: 14px;
  }
  .publisher-mark {
    width: 38px;
    height: 38px;
    border-radius: 50%;
    background: var(--title-white);
  }
  .publisher-name {
    font-family: "Libre Baskerville", serif;
    font-weight: 700;
    font-size: 22px;
    color: var(--title-white);
  }
</style>
</head>
<body>
  <main class="book-cover">
    <div class="cover-artwork" role="img" aria-label="Painted abstract background in deep and sky blue brush strokes"></div>
    <div class="spine-edge"></div>

    <h1 class="title-block" aria-label="The Quiet Ascent">
      <span class="title-the">The</span>
      <span class="title-quiet">Quiet</span>
      <span class="title-ascent">Ascent</span>
    </h1>

    <svg class="butterfly-illustration" viewBox="0 0 466 280" role="img" aria-label="Illustration of a pink and golden butterfly with open wings">
      <defs>
        <radialGradient id="wingGlow" cx="50%" cy="50%" r="50%">
          <stop offset="0%" stop-color="#f7c86a"/>
          <stop offset="35%" stop-color="#e94fc8" stop-opacity="0.85"/>
          <stop offset="70%" stop-color="#e94fc8" stop-opacity="0.3"/>
          <stop offset="100%" stop-color="#e94fc8" stop-opacity="0"/>
        </radialGradient>
      </defs>
      <ellipse cx="233" cy="130" rx="228" ry="135" fill="url(#wingGlow)"/>
    </svg>

    <p class="subtitle">Lessons of Insight From A Circle of Mentors<br>to Guide You Toward a Fuller Journey</p>

    <p class="author">Dr. Marisol Penbury Aldane</p>

    <div class="publisher">
      <span class="publisher-mark"></span>
      <span class="publisher-name">The Lark Publishing House</span>
    </div>
  </main>
</body>
</html>
```